Business Card Design

Provide project management services to the construction and other industries
Construction services - Civil and Concrete works
Shop Detailing
Structural Modelling
Client side coordination of project teams and consultants
Feasibility Studies for construction projects

Industry/Entity Type

Business

Contact Information for Business Card

Plan Sure
Derek Calloway B.Sc (Hons), M.P.M.
Principal

m: 0412 738 564
e: dcalloway@plansure.com.au

p: 08 6358 2714
a: 17 Banksia Court, Kelmscott, WA 6111

```html
<!DOCTYPE html>
<html lang="en">
<head>
<meta charset="utf-8">
<title>Plan Sure – Business Card</title>
<link rel="stylesheet" href="https://fonts.googleapis.com/css2?family=Lato:wght@400;700;900&display=swap">
<style>
  :root {
    --backdrop: #2b2b2b;
    --card-white: #ffffff;
    --card-shade: #ececec;
    --card-black: #050505;
    --brand-green: #1f8a1f;
    --text-light: #d9d9d9;
    --logo-ink: #111111;
  }
  * { box-sizing: border-box; margin: 0; padding: 0; }
  html, body {
    width: 1200px; height: 997px; overflow: hidden;
    background: var(--backdrop);
    font-family: "Lato", Arial, sans-serif;
  }
  .stage { position: relative; width: 1200px; height: 997px; }

  .card {
    position: absolute;
    width: 560px; height: 320px;
    border-radius: 22px;
    overflow: hidden;
    background: linear-gradient(180deg, var(--card-white) 0%, var(--card-shade) 100%);
    box-shadow: 0 18px 40px rgba(0,0,0,.55);
  }
  .card--front { left: 60px; top: 130px; }
  .card--back  { left: 580px; top: 530px; }
  .card__shape { position: absolute; inset: 0; }

  .wordmark {
    position: absolute;
    font-weight: 900;
    color: var(--logo-ink);
    letter-spacing: 1px;
    white-space: nowrap;
  }
  .card--front .wordmark {
    left: 150px; top: 120px; font-size: 50px;
    transform: rotate(-11.3deg); transform-origin: left center;
  }
  .card--back .wordmark {
    left: 140px; top: 70px; font-size: 46px;
    transform: rotate(-12deg); transform-origin: left center;
  }

  .website {
    position: absolute;
    left: 280px; top: 232px;
    color: var(--text-light);
    font-size: 17px; letter-spacing: 4px;
    transform: rotate(-11.3deg); transform-origin: left center;
  }

  .person { position: absolute; left: 28px; top: 232px; }
  .person__name { color: #ffffff; font-weight: 700; font-size: 22px; letter-spacing: .5px; }
  .person__role { color: var(--brand-green); font-weight: 700; font-size: 13px; margin-top: 6px; line-height: 1.55; }

  .contact {
    position: absolute; right: 22px; top: 150px;
    list-style: none; text-align: right;
    color: var(--text-light); font-size: 13px; letter-spacing: .5px;
  }
  .contact li { display: flex; justify-content: flex-end; align-items: center; gap: 7px; height: 22px; }
  .contact svg { width: 12px; height: 12px; fill: var(--brand-green); flex: none; }
</style>
</head>
<body>
<main class="stage">

  <section class="card card--front" aria-label="Card front">
    <svg class="card__shape" viewBox="0 0 560 320" aria-hidden="true">
      <path d="M0 262 L276 206 L288 216 L300 202 L560 150 L560 320 L0 320 Z" fill="var(--card-black)"/>
      <path d="M0 262 L276 206 L288 216 L300 202 L560 150" fill="none" stroke="var(--brand-green)" stroke-width="5"/>
    </svg>
    <div class="wordmark">PLAN SURE</div>
    <div class="website">www.plansure.com.au</div>
  </section>

  <section class="card card--back" aria-label="Card back">
    <svg class="card__shape" viewBox="0 0 560 320" aria-hidden="true">
      <path d="M0 212 L58 212 L70 222 L82 210 L560 92 L560 320 L0 320 Z" fill="var(--card-black)"/>
      <path d="M0 212 L58 212 L70 222 L82 210 L560 92" fill="none" stroke="var(--brand-green)" stroke-width="5"/>
    </svg>
    <div class="wordmark">PLAN SURE</div>

    <div class="person">
      <p class="person__name">DEREK CALLOWAY</p>
      <p class="person__role">B.SC (HONS), M.P.M.<br>PRINCIPAL</p>
    </div>

    <ul class="contact">
      <li>0412 738 564
        <svg viewBox="0 0 12 12"><path d="M3 0h6a1 1 0 0 1 1 1v10a1 1 0 0 1-1 1H3a1 1 0 0 1-1-1V1a1 1 0 0 1 1-1zm0 1.5v8h6v-8z"/></svg></li>
      <li>08 6358 2714
        <svg viewBox="0 0 12 12"><path d="M1 4c0-2 2-3 5-3s5 1 5 3v1H8V4H4v1H1zM3 6h6l2 5H1z"/></svg></li>
      <li>DCALLOWAY@PLANSURE.COM.AU
        <svg viewBox="0 0 12 12"><path d="M0 2h12v8H0zm1 1v.4l5 3.2 5-3.2V3zm0 1.6V9h10V4.6L6 7.8z"/></svg></li>
      <li>17 BANKSIA COURT, KELMSCOTT, WA 6111
        <svg viewBox="0 0 12 12"><path d="M6 0a4 4 0 0 1 4 4c0 3-4 8-4 8S2 7 2 4a4 4 0 0 1 4-4zm0 2.5a1.5 1.5 0 1 0 0 3 1.5 1.5 0 0 0 0-3z"/></svg></li>
    </ul>
  </section>

</main>
</body>
</html>
```